App Design Project

We had an tavrix/vemo app built (freelancer), without any real design applied. Currently just made up of plain buttons and text. No colors, images, etc.
App is about 20 total pages, and contains a login window, a main menu, and then several different options that pull data via web services from our back-end.
About the app:
The application will be used by physicians, who are in essence speakers who are speaking on behalf of pharmaceutical companies, to train doctors on the use of their products. They will use the app to get a list of their upcoming speaking engagements, calendars, access to slide presentations, and the ability for them to submit expense forms with pictures of receipts, etc.
We need the following things:
* An App Icon
* An Tavrix startup screen
* Two Vemo startup screens (one portrait and one landscape)
* Color schedme recommendations for the pages
* Page design recommendations: header/footer
The Tavrix and Vemo startup screens are screens displayed while the app is loading (splash screen). They are simply a large version of the app's logo (with differing dimensions) and maybe some extra detail as the space allows more. The Vemo and Tavrix screens can be identical, but please note the size. orientation and aspect ratio differences.
Objects possibilities...(pick any/none/anything else that is appropriate):
* Person behind a podium
* Someone speaking / presenting
* be creative
Styles we like:
This is for pharma, so medical might be appropriate
open to recommendations
Keep in mind that we are looking for page design recommendations as well. We could provide sample screens with text, and then are looking for recommendations on color, and general page design.
A successful designer may also win several other apps currently under consideration.

```html
<!DOCTYPE html>
<html lang="en">
<head>
<meta charset="utf-8">
<title>Pellora Speaker Resource Center – Sign In</title>
<link rel="stylesheet" href="https://fonts.googleapis.com/css2?family=Julius+Sans+One&family=Didact+Gothic&display=swap">
<style>
  :root {
    --bg-centre: #fffdf7;
    --bg-mid: #f8ecd2;
    --bg-edge: #eed9ae;
    --ink: #2b2b2b;
    --ink-soft: #4a4a4a;
    --field-fill: rgba(240, 226, 196, 0.85);
    --field-edge: rgba(214, 196, 160, 0.9);
    --field-text: #cbb894;
    --panel: rgba(255, 250, 238, 0.55);
    --go: #9fd88f;
    --go-edge: #86c474;
    --go-text: #f4fbef;
    --footer: #8d8d8d;
  }
  * { box-sizing: border-box; margin: 0; padding: 0; }
  html, body { width: 900px; height: 1200px; overflow: hidden; }
  body {
    position: relative;
    font-family: "Didact Gothic", sans-serif;
    background: radial-gradient(ellipse 75% 60% at 50% 42%, var(--bg-centre) 0%, var(--bg-mid) 55%, var(--bg-edge) 100%);
  }
  .brand {
    position: absolute;
    top: 470px;
    left: 0;
    width: 900px;
    text-align: center;
  }
  .brand-name {
    font-family: "Julius Sans One", sans-serif;
    font-size: 104px;
    letter-spacing: 6px;
    color: var(--ink);
    line-height: 1;
  }
  .brand-tagline {
    margin-top: 44px;
    font-family: "Julius Sans One", sans-serif;
    font-size: 27px;
    letter-spacing: 4px;
    color: var(--ink-soft);
  }
  .login-panel {
    position: absolute;
    top: 1044px;
    left: 114px;
    width: 672px;
    height: 84px;
    border-radius: 10px;
    background: var(--panel);
  }
  .field, .login-button {
    position: absolute;
    top: 12px;
    height: 60px;
    border-radius: 6px;
    display: flex;
    align-items: center;
    justify-content: center;
    font-size: 20px;
  }
  .field {
    width: 264px;
    background: var(--field-fill);
    border: 2px solid var(--field-edge);
    color: var(--field-text);
  }
  .field-username { left: 12px; }
  .field-password { left: 297px; }
  .login-button {
    left: 576px;
    width: 84px;
    background: var(--go);
    border: 2px solid var(--go-edge);
    color: var(--go-text);
  }
  .footer-bar {
    position: absolute;
    bottom: 0;
    left: 0;
    width: 900px;
    height: 36px;
    background: var(--footer);
  }
</style>
</head>
<body>
  <header class="brand">
    <h1 class="brand-name">Pellora</h1>
    <p class="brand-tagline">Speaker Resource Center</p>
  </header>

  <form class="login-panel">
    <div class="field field-username">Username</div>
    <div class="field field-password">Password</div>
    <div class="login-button">Log In</div>
  </form>

  <footer class="footer-bar"></footer>
</body>
</html>
```